LEAP GLOW SWAY II (POSTCARD DESIGN)

Hello our original designer is no longer on this platform. We want to use design #51937604 with some minor adjustments. I've uploaded the original project 1) change the date on the front of card (keeping the same format) to August 27 with a start time of 2:30 PM.
2) on the front part of the card I want to include a splash graphic that says Back By Popular Demand! 3) replace pictures on the front with the attached photo. make it blend in. 3) Use the same photo on the back of the card.
Let the post card examples serve as template examples and let your creativity flourish! This is time sensitive so get these to me fast! If you're early you may win. thx

```html
<!DOCTYPE html>
<html lang="en">
<head>
<meta charset="utf-8">
<title>Leap Glow Sway – Postcard</title>
<link rel="stylesheet" href="https://fonts.googleapis.com/css2?family=Montserrat:ital,wght@0,400;0,500;0,700;0,800;0,900;1,700;1,800;1,900&family=Roboto+Condensed:wght@700;800&display=swap">
<style>
  :root {
    --ink: #141416;
    --white: #ffffff;
    --pink: #e4187d;
    --pink-deep: #b5125f;
    --cyan: #19d3dc;
    --blue: #1e6fd0;
    --yellow: #ffc20e;
    --pill: #3d6f93;
  }
  * { margin: 0; padding: 0; box-sizing: border-box; }
  html, body { width: 1200px; height: 800px; overflow: hidden; background: var(--ink); }
  .postcard {
    position: relative; width: 1200px; height: 800px; overflow: hidden;
    background:
      repeating-linear-gradient(125deg, rgba(255,255,255,0.03) 0 60px, rgba(0,0,0,0.1) 60px 120px),
      radial-gradient(ellipse at 45% 40%, #3a3a3f 0%, var(--ink) 70%);
    font-family: "Montserrat", sans-serif;
    color: var(--white);
  }
  .backdrop { position: absolute; inset: 0; }
  .presenter {
    position: absolute; left: 52px; top: 46px;
    color: var(--pink); font-size: 23px; font-weight: 500; line-height: 1.15;
    letter-spacing: 0.5px; text-transform: uppercase;
  }
  .title {
    position: absolute; left: 50px; top: 128px;
    font-weight: 800; font-style: italic; text-transform: uppercase;
    line-height: 1;
  }
  .title-line { display: block; font-size: 72px; height: 72px; letter-spacing: 1px; transform: scaleX(1.2); transform-origin: left; }
  .title-accent {
    display: block; font-size: 118px; font-weight: 900; letter-spacing: 3px; margin-top: 16px;
    transform: scaleX(1.12); transform-origin: left;
    background: linear-gradient(90deg, var(--blue) 0%, var(--cyan) 50%, var(--pink) 85%);
    -webkit-background-clip: text; background-clip: text; color: transparent;
  }
  .schedule {
    position: absolute; left: 50px; top: 428px;
    display: flex; align-items: center;
    font-family: "Roboto Condensed", sans-serif; font-weight: 800;
  }
  .day { font-size: 104px; color: var(--cyan); line-height: 1; }
  .month-year { margin-left: 10px; line-height: 0.95; font-family: "Montserrat", sans-serif; font-weight: 800; }
  .month { display: block; font-size: 40px; }
  .year { display: block; font-size: 50px; font-style: italic; }
  .divider { width: 0; height: 100px; border-left: 4px dashed var(--pink); margin: 0 18px; }
  .time { font-size: 104px; line-height: 1; color: var(--cyan); }
  .time-suffix { color: var(--white); }
  .venue { position: absolute; left: 50px; top: 545px; display: flex; gap: 12px; }
  .venue-icon { width: 26px; height: 34px; margin-top: 6px; }
  .venue-name { font-size: 34px; font-weight: 500; letter-spacing: 0.5px; line-height: 1.1; text-transform: uppercase; }
  .venue-city { font-size: 26px; font-weight: 500; }
  .tickets { position: absolute; left: 60px; top: 660px; display: flex; align-items: center; gap: 12px; }
  .tickets-square { width: 40px; height: 40px; background: var(--pink); }
  .tickets-label { color: var(--yellow); font-size: 20px; font-weight: 800; line-height: 1.25; }
  .box-office { position: absolute; left: 243px; top: 652px; }
  .box-office-label { font-size: 21px; font-weight: 700; }
  .box-office-phone { font-size: 26px; font-weight: 900; font-style: italic; color: var(--pink); letter-spacing: 0.5px; }
  .box-office-link {
    position: absolute; left: 243px; top: 717px; width: 357px; height: 40px;
    border-radius: 0 20px 20px 0;
    background: linear-gradient(90deg, var(--pill), #5287ad);
    font-size: 20px; font-weight: 800; letter-spacing: 2px;
    line-height: 40px; padding-left: 14px;
  }
  .callout { position: absolute; left: 570px; top: 0; width: 340px; height: 310px; }
  .callout-top {
    position: absolute; left: 663px; top: 42px; width: 216px; height: 78px;
    background: var(--yellow); color: var(--ink);
    font-size: 58px; font-weight: 900; font-style: italic; text-align: center; line-height: 78px;
  }
  .callout-sub {
    position: absolute; left: 585px; top: 148px; width: 290px;
    color: var(--yellow); text-align: center;
    font-size: 26px; font-weight: 900; font-style: italic; line-height: 1.25; letter-spacing: 1.5px;
    text-transform: uppercase;
  }
  .portrait {
    position: absolute; left: 735px; top: 50px; width: 465px; height: 750px;
    background: linear-gradient(180deg, #2b2220 0%, #5a4038 22%, #e9e6e2 42%, #f3f1ee 100%);
    clip-path: polygon(28% 0, 74% 0, 80% 33%, 100% 38%, 100% 100%, 0 100%, 2% 44%, 22% 33%);
  }
</style>
</head>
<body>
<main class="postcard">
  <svg class="backdrop" width="1200" height="800" viewBox="0 0 1200 800" aria-hidden="true">
    <defs>
      <linearGradient id="violet-field" x1="0" y1="0" x2="1" y2="1">
        <stop offset="0" stop-color="#5b3480"/>
        <stop offset="1" stop-color="#2a1840"/>
      </linearGradient>
    </defs>
    <polygon points="1010,0 1200,0 1200,520 1090,520" fill="url(#violet-field)"/>
    <polygon points="760,800 1010,0 1080,0 850,800" fill="var(--pink)"/>
    <polygon points="1040,0 1110,0 1200,300 1200,520" fill="var(--pink-deep)" opacity="0.7"/>
  </svg>

  <p class="presenter">Brightstep Productions presents<br>Nova Reyes's</p>

  <h1 class="title">
    <span class="title-line">Leap</span>
    <span class="title-line">Glow</span>
    <span class="title-accent">Sway</span>
  </h1>

  <div class="schedule">
    <span class="day">27</span>
    <span class="month-year"><span class="month">AUGUST</span><span class="year">2023</span></span>
    <span class="divider"></span>
    <span class="time">2:30<span class="time-suffix">PM</span></span>
  </div>

  <div class="venue">
    <svg class="venue-icon" viewBox="0 0 26 34" aria-hidden="true">
      <path d="M13 1C6.4 1 1 6.3 1 12.8 1 21.5 13 33 13 33s12-11.5 12-20.2C25 6.3 19.6 1 13 1z" fill="var(--pink)"/>
      <circle cx="13" cy="12.5" r="4.5" fill="var(--ink)"/>
    </svg>
    <div>
      <p class="venue-name">Harbor Light Theatre</p>
      <p class="venue-city">Maple Grove, CA</p>
    </div>
  </div>

  <div class="tickets">
    <span class="tickets-square" aria-hidden="true"></span>
    <p class="tickets-label">Buy<br>Tickets</p>
  </div>

  <div class="box-office">
    <p class="box-office-label">Box Office</p>
    <p class="box-office-phone">(555) 210-STEP</p>
  </div>
  <p class="box-office-link">www.example.com/lgs</p>

  <div class="portrait" role="img" aria-label="Portrait photo of the featured choreographer in a white blazer"></div>

  <svg class="callout" viewBox="570 0 340 310" aria-hidden="true">
    <polygon points="860,0 905,0 905,8 920,8 905,30 860,40" fill="var(--yellow)"/>
    <polygon points="838,0 870,0 870,245 838,245" fill="var(--pink)"/>
    <rect x="577" y="88" width="268" height="157" fill="var(--ink)"/>
    <polygon points="580,245 760,245 680,300 700,260" fill="var(--pink)"/>
  </svg>
  <p class="callout-top">BACK</p>
  <p class="callout-sub">By popular<br>demand!</p>
</main>
</body>
</html>
```